BEACON CABS

Taxi card design

Need changes very slow in replying to my messages.

Target Market(s)

Customers

Industry/Entity Type

Taxi

Contact Information for Business Card

See previous design

Font styles to use
Sans Serif

Colors
A7469A
B969AE
D3A5CF
EDDBEB
F8F0F9
6B429C
8869AF
B7A5CE
E3DAEB
F3F0F8

Requirements
Nice to have
• We are in the business of looking after people, not just driving vehicles front
Should not have
• Front number 01632 480 480 needs to big big

```html
<!DOCTYPE html>
<html lang="en">
<head>
<meta charset="utf-8">
<title>Beacon Cabs – Business Card</title>
<link href="https://fonts.googleapis.com/css2?family=Michroma&family=Poppins:wght@400;600&display=swap" rel="stylesheet">
<style>
  :root{
    --plum:#A7469A;
    --violet:#6B429C;
    --violet-mid:#8869AF;
    --ink:#111111;
    --paper:#ffffff;
    --stage:#2a2a2e;
    --brand-grad:linear-gradient(135deg,var(--plum) 0%,var(--violet) 100%);
    --bar-grad:linear-gradient(90deg,var(--plum) 0%,var(--violet) 100%);
  }
  *{box-sizing:border-box;margin:0;padding:0}
  html,body{width:1200px;height:1200px;overflow:hidden}
  body{background:var(--stage);position:relative;font-family:"Poppins",sans-serif}
  .card{position:absolute;left:150px;width:900px;height:514px;overflow:hidden;border-radius:4px;box-shadow:0 10px 30px rgba(0,0,0,.45)}
  .card--front{top:56px;background:var(--brand-grad)}
  .card--back{top:630px;background:var(--paper)}

  .wordmark{font-family:"Michroma",sans-serif;font-weight:400;letter-spacing:2px;white-space:nowrap}
  .front-wordmark{position:absolute;top:150px;left:0;width:100%;text-align:center;font-size:62px;color:var(--paper)}

  .front-band{position:absolute;left:0;top:300px;width:100%;height:90px;background:var(--paper);display:flex;align-items:center;justify-content:center;gap:22px}
  .front-number{font-family:"Michroma",sans-serif;font-size:46px;color:var(--ink);letter-spacing:4px;white-space:nowrap}
  .icon-tile{display:flex;align-items:center;justify-content:center;border-radius:8px;flex:none}
  .icon-tile--brand{width:60px;height:60px;background:var(--brand-grad)}
  .icon-tile--light{width:40px;height:40px;background:var(--paper);border-radius:7px}
  .icon-tile svg{width:62%;height:62%}

  .back-wordmark{position:absolute;top:56px;left:40px;font-size:40px;color:var(--ink)}

  .services{position:absolute;top:70px;left:496px;width:264px;text-align:center;font-family:"Michroma",sans-serif;font-size:14px;line-height:1.8;color:var(--ink);letter-spacing:.5px;white-space:nowrap}

  .lines{position:absolute;left:24px;top:180px;display:flex;flex-direction:column;gap:30px}
  .line-pill{width:420px;height:62px;border-radius:12px;background:var(--bar-grad);display:flex;align-items:center;gap:16px;padding-left:14px}
  .line-number{font-family:"Michroma",sans-serif;font-size:25px;color:var(--paper);letter-spacing:3px;white-space:nowrap}

  .address{position:absolute;left:472px;top:220px;font-size:18px;line-height:1.5;color:var(--ink);font-style:normal;white-space:nowrap}
  .contact{position:absolute;left:472px;top:370px;font-size:16px;line-height:1.75;color:var(--ink);white-space:nowrap}
  .contact dt{display:inline;color:var(--plum);font-weight:600}
  .contact dd{display:inline}
  .contact dd::after{content:"";display:block}

  .side-strip{position:absolute;right:0;top:0;width:120px;height:100%;background:linear-gradient(180deg,var(--plum) 0%,var(--violet) 100%);display:flex;flex-direction:column;align-items:center;justify-content:flex-end;padding-bottom:26px;gap:22px}
  .side-number{writing-mode:vertical-rl;transform:rotate(180deg);font-family:"Michroma",sans-serif;font-size:28px;color:var(--paper);letter-spacing:3px;white-space:nowrap}
  .side-strip .icon-tile--light{width:56px;height:56px}
</style>
</head>
<body>
<svg width="0" height="0" style="position:absolute" aria-hidden="true">
  <symbol id="handset" viewBox="0 0 24 24">
    <path fill="currentColor" d="M6.6 10.8c1.4 2.8 3.8 5.1 6.6 6.6l2.2-2.2c.3-.3.7-.4 1-.2 1.1.4 2.300.6 3.6.6.6 0 1 .4 1 1V20c0 .6-.4 1-1 1C10.6 21 3 13.4 3 4c0-.6.4-1 1-1h3.5c.6 0 1 .4 1 1 0 1.3.2 2.5.6 3.6.1.3 0 .7-.2 1L6.6 10.8z"/>
  </symbol>
</svg>

<section class="card card--front" aria-label="Card front">
  <h1 class="wordmark front-wordmark">BEACON CABS</h1>
  <div class="front-band">
    <span class="icon-tile icon-tile--brand" style="color:var(--paper)"><svg><use href="#handset"/></svg></span>
    <span class="front-number">01632 480 480</span>
  </div>
</section>

<section class="card card--back" aria-label="Card back">
  <h2 class="wordmark back-wordmark">BEACON CABS</h2>

  <p class="services">AIRPORT TRANSFERS<br>MINIBUSES<br>SCHOOL TRANSPORT</p>

  <div class="lines">
    <div class="line-pill"><span class="icon-tile icon-tile--light" style="color:var(--plum)"><svg><use href="#handset"/></svg></span><span class="line-number">01632 960 111</span></div>
    <div class="line-pill"><span class="icon-tile icon-tile--light" style="color:var(--plum)"><svg><use href="#handset"/></svg></span><span class="line-number">01632 960 222</span></div>
    <div class="line-pill"><span class="icon-tile icon-tile--light" style="color:var(--plum)"><svg><use href="#handset"/></svg></span><span class="line-number">01632 960 333</span></div>
  </div>

  <address class="address">Oak Lane Community Hall<br>Market Row<br>Brackenford<br>ZZ1 4AB</address>

  <dl class="contact">
    <dt>Freephone:</dt> <dd>0808 157 0 444</dd>
    <dt>Email:</dt> <dd>hello@beaconcabs.example</dd>
    <dt>Website:</dt> <dd>www.beaconcabs.example</dd>
  </dl>

  <div class="side-strip">
    <span class="side-number">01632 480 480</span>
    <span class="icon-tile icon-tile--light" style="color:var(--plum)"><svg><use href="#handset"/></svg></span>
  </div>
</section>
</body>
</html>
```